Home inspection business! professional look attracting customers just by looks. Read must haves

its a new business I started on my own for home inspections I would like something very professional to give to real estate agents and clients, its going to have my license number on it my business phone number my name my website as well etc on the back side it will be servicing areas and also what kind of services I offer I also have a business card from someone else the way I would like mine to be. I will attach my logo

Home Inspection

listed in nice to haves

• phone number - 555 293 8471
• website- hollowpinecheck.com
• license number #2938475610
• my name Gavin keropulis
• picture of my logo and me on the front
• on the back of the card. stating I am servicing All of New York and Long Island
• also services I will offer will be home inspection -mold inspection -lead inspection -radon inspection -Termite Inspection -Infared Scan.
• and also we provide inspections for single family homes condos co-ops town-homes
• and commercial property
• same colors as the logos and also if you recommend fonts to look like the logo not sure up to you

```html
<!DOCTYPE html>
<html lang="en">
<head>
<meta charset="utf-8">
<title>Hollow Pine Check Home Inspectors – Business Card</title>
<link href="https://fonts.googleapis.com/css2?family=Lato:wght@400;700&display=swap" rel="stylesheet">
<style>
  :root {
    --brand-blue: #4fa0d9;
    --ink-gray: #5a5a5a;
    --card-white: #ffffff;
    --backdrop: #e9e6e2;
  }
  * { box-sizing: border-box; margin: 0; padding: 0; }
  html, body { width: 1200px; height: 1200px; overflow: hidden; }
  body {
    background: var(--backdrop);
    font-family: "Lato", Arial, sans-serif;
    position: relative;
  }
  .card {
    position: absolute;
    left: 267px;
    width: 670px;
    height: 390px;
    background: var(--card-white);
    box-shadow: 0 2px 8px rgba(0,0,0,0.18);
    overflow: hidden;
  }
  .card--front { top: 166px; }
  .card--back { top: 606px; }

  .portrait {
    position: absolute;
    left: 26px; top: 22px;
    width: 302px; height: 347px;
  }

  .brand {
    position: absolute;
    right: 40px;
    top: 70px;
    display: flex;
    align-items: center;
    gap: 8px;
    color: var(--ink-gray);
    font-weight: 700;
    font-size: 19px;
    letter-spacing: 0.5px;
    text-transform: uppercase;
    white-space: nowrap;
  }
  .brand__dot {
    width: 14px; height: 14px;
    border-radius: 50%;
    background: var(--brand-blue);
  }
  .brand__name { line-height: 1.2; }

  .contact { position: absolute; right: 40px; text-align: right; }
  .contact__name {
    top: 172px;
    color: var(--brand-blue);
    font-size: 21px;
    font-weight: 700;
    text-transform: uppercase;
  }
  .contact__role {
    top: 199px;
    color: var(--ink-gray);
    font-size: 19px;
  }
  .contact__line {
    right: 40px;
    display: flex;
    align-items: center;
    gap: 4px;
    color: var(--ink-gray);
    font-size: 20px;
    font-weight: 700;
  }
  .contact__line svg { width: 28px; height: 28px; }
  .contact__phone { top: 261px; }
  .contact__web { top: 296px; font-weight: 400; }
  .contact__license {
    top: 334px;
    color: var(--brand-blue);
    font-size: 23px;
    font-weight: 700;
  }

  .service-area {
    position: absolute;
    left: 42px; top: 28px;
    width: 340px;
    color: var(--ink-gray);
    font-size: 22px;
    font-weight: 700;
    line-height: 34px;
  }
  .service-list {
    position: absolute;
    left: 42px; top: 96px;
    list-style: none;
    color: var(--brand-blue);
    font-size: 21px;
    font-weight: 700;
    line-height: 26.8px;
  }
  .card--back .brand { top: 92px; }
</style>
</head>
<body>
  <section class="card card--front">
    <svg class="portrait" viewBox="0 0 302 347" role="img" aria-label="Portrait photo of Gavin Keropulis">
      <polygon points="151,0 302,87 302,260 151,347 0,260 0,87" fill="#4fa0d9"/>
    </svg>

    <div class="brand">
      <span class="brand__dot"></span>
      <span class="brand__name">Hollow Pine Check</span>
    </div>

    <p class="contact contact__name">Gavin Keropulis</p>
    <p class="contact contact__role">Director</p>

    <p class="contact contact__line contact__phone">555 293 8471
      <svg viewBox="0 0 28 28" aria-hidden="true">
        <circle cx="14" cy="14" r="12.5" fill="none" stroke="#4fa0d9" stroke-width="1.6"/>
        <path d="M10 8.5c-.8.4-1.6 1.4-1.3 2.9.6 3 3.3 6.2 6.4 7.7 1.4.7 2.6.2 3.2-.6l-2.4-2.2-1.4.9c-1.4-.7-2.7-2.2-3.3-3.6l1-1.3z" fill="#4fa0d9"/>
      </svg>
    </p>
    <p class="contact contact__line contact__web">hollowpinecheck.com
      <svg viewBox="0 0 28 28" aria-hidden="true">
        <circle cx="14" cy="14" r="12.5" fill="none" stroke="#4fa0d9" stroke-width="1.6"/>
        <circle cx="14" cy="14" r="8" fill="none" stroke="#4fa0d9" stroke-width="1.2"/>
        <ellipse cx="14" cy="14" rx="3.5" ry="8" fill="none" stroke="#4fa0d9" stroke-width="1.2"/>
        <path d="M6 14h16M7.5 10h13M7.5 18h13" stroke="#4fa0d9" stroke-width="1.2"/>
      </svg>
    </p>
    <p class="contact contact__license">license number #2938475610</p>
  </section>

  <section class="card card--back">
    <p class="service-area">Servicing All of New York and Long Island</p>
    <ul class="service-list">
      <li>Inspection -mold</li>
      <li>Inspection -lead</li>
      <li>Inspection -radon</li>
      <li>Inspection -Termite</li>
      <li>Inspection -Infared Scan.</li>
      <li>And also we provide</li>
      <li>Inspections for</li>
      <li>Single family homes</li>
      <li>Condos co-ops town-homes</li>
      <li>And commercial property</li>
    </ul>
    <div class="brand">
      <span class="brand__dot"></span>
      <span class="brand__name">Hollow Pine Check</span>
    </div>
  </section>
</body>
</html>
```